Responsive webpage design for an exsiting layout (romain catholic church)

Example of content and layout on: [url removed, login to view]

header: "Seelsorgekreis Hollbachtal Ost" and the banners (attachement)
The mainmenu entires will be "Pastoralraum", "Ebersried", "Kalmbach", "Lindenau", "Rothalden", "Steinweiler", "Zweckverband".
however new entries may follow.
The submenus are different (like on example page)

We need:
- new design (should not look like the other page)
- responsive design
- the colors and design should be matching for a romain catholic church (liturgical colors)
- the page should be "light" (not too much dark colors, background...)

```html
<!DOCTYPE html>
<html lang="de">
<head>
<meta charset="utf-8">
<title>Seelsorgekreis Hollbachtal Ost</title>
<link href="https://fonts.googleapis.com/css2?family=Arimo:ital,wght@0,400;0,700;1,400&display=swap" rel="stylesheet">
<style>
:root{
  --purple:#6a2c9c;
  --purple-mid:#7b3aa8;
  --purple-light:#a868d8;
  --purple-pale:#efe6f6;
  --text:#333;
  --line:#d8d8d8;
  --panel-head:#f3f3f3;
}
*{box-sizing:border-box;margin:0;padding:0}
html,body{width:1178px;height:1200px;overflow:hidden;background:#fff}
body{font-family:"Arimo",Arial,sans-serif;color:var(--text);position:relative}
.site-title{position:absolute;left:195px;top:6px;color:var(--purple);font-size:28px;line-height:33px;font-weight:400}
.parish-badges{position:absolute;left:606px;top:6px;display:flex;gap:22px}
.parish-badge{width:58px;height:70px;border:1px solid #ddd;border-radius:4px;display:flex;align-items:center;justify-content:center;background:#fff}
.parish-badge span{width:40px;height:48px;border-radius:4px;background:var(--purple-pale);border:1px solid #cbb6dc}
.main-nav{position:absolute;left:129px;top:116px;display:flex;align-items:center;height:32px}
.main-nav a{font-size:12px;color:#333;text-decoration:none;padding:0 18px;line-height:32px}
.main-nav a.active{background:var(--purple-mid);color:#fff;font-weight:700;border-radius:3px;margin-right:2px}
.search{position:absolute;left:827px;top:118px;display:flex;height:28px}
.search input{width:152px;border:1px solid #ccc;border-radius:3px 0 0 3px;height:28px}
.search button{width:56px;border:1px solid #ccc;border-left:none;background:#fff;border-radius:0 3px 3px 0;font-family:inherit;font-size:12px;color:#333}
.slider{position:absolute;left:116px;top:167px;width:932px;height:328px;box-shadow:0 2px 6px rgba(0,0,0,.4)}
.slider .photo{width:100%;height:100%;background:radial-gradient(circle at 50% 18%,#e9e4d2 0,#2c4a88 8%,#b99340 16%,#7a5a2a 40%,#c9a45a 65%,#5a4025 100%)}
.slider .arrow{position:absolute;top:148px;width:32px;height:32px}
.slider .prev{left:8px}.slider .next{right:8px}
.welcome{position:absolute;left:0;width:1178px;top:510px;text-align:center;color:var(--purple);font-size:28px;font-weight:400}
.side-nav{position:absolute;left:134px;top:556px;width:213px;list-style:none}
.side-nav li{height:34px;line-height:34px;padding-left:13px;font-size:12px;border-bottom:1px solid var(--purple-mid)}
.side-nav li.active{background:var(--purple-light);color:#fff;font-weight:700;border-bottom:none}
.impuls{position:absolute;left:373px;top:556px;width:693px;height:316px;border:1px solid var(--line);border-radius:3px}
.impuls h2{height:45px;background:var(--panel-head);border-bottom:1px solid var(--line);font-size:24px;font-weight:400;line-height:45px;padding-left:12px;color:#222}
.impuls .copy{position:absolute;left:12px;top:57px;width:330px;font-size:11px;line-height:15px}
.impuls .copy p{margin-bottom:15px}
.impuls .picture{position:absolute;left:358px;top:55px;width:322px;height:248px;background:radial-gradient(circle at 45% 55%,#e3b25a 0,#9a6a25 35%,#3a220c 80%)}
.news-badge{position:absolute;left:150px;top:930px;width:106px;height:106px;border-radius:6px;background:var(--purple-pale);border:1px solid #cbb6dc}
.news{position:absolute;left:296px;width:771px;display:grid;grid-template-columns:repeat(4,1fr);border-bottom:2px dotted var(--purple-mid);padding-bottom:10px}
.news.row1{top:932px}.news.row2{top:1032px}
.news div{text-align:center;font-size:11px;line-height:16px;color:var(--purple);border-left:1px solid var(--purple-mid);height:64px}
.news div:first-child{border-left:none}
.news strong{display:block;color:#333}
.news em{font-style:italic}
.bottom-bar{position:absolute;left:138px;top:1131px;width:932px;height:40px;border:1px solid var(--line);border-radius:3px;display:flex;align-items:center;justify-content:center}
</style>
</head>
<body>
<header>
  <h1 class="site-title">Seelsorgekreis<br>Hollbachtal Ost</h1>
  <div class="parish-badges" aria-label="Pfarreien">
    <div class="parish-badge"><span></span></div>
    <div class="parish-badge"><span></span></div>
    <div class="parish-badge"><span></span></div>
    <div class="parish-badge"><span></span></div>
    <div class="parish-badge"><span></span></div>
  </div>
  <nav class="main-nav">
    <a class="active" href="#">Pastoralraum</a><a href="#">Ebersried</a><a href="#">Kalmbach</a><a href="#">Lindenau</a><a href="#">Rothalden</a><a href="#">Steinweiler</a><a href="#">Zweckverband</a>
  </nav>
  <form class="search"><input type="text" aria-label="Suche"><button type="button">Search</button></form>
</header>

<section class="slider">
  <div class="photo" role="img" aria-label="Foto einer reich verzierten Kirchenkuppel mit Mosaiken in Gold und Blau"></div>
  <svg class="arrow prev" viewBox="0 0 32 32"><circle cx="16" cy="16" r="15" fill="#fff" opacity=".85"/><path d="M19 9l-7 7 7 7" stroke="#333" stroke-width="3" fill="none"/></svg>
  <svg class="arrow next" viewBox="0 0 32 32"><circle cx="16" cy="16" r="15" fill="#fff" opacity=".85"/><path d="M13 9l7 7-7 7" stroke="#333" stroke-width="3" fill="none"/></svg>
</section>

<h2 class="welcome">Herzlich Willkommen</h2>

<ul class="side-nav">
  <li class="active">Cras justo odio</li>
  <li>Dapibus ac facilisis in</li>
  <li>Morbi leo risus</li>
  <li>Porta ac consectetur ac</li>
  <li>Vestibulum at eros</li>
</ul>

<article class="impuls">
  <h2>Impuls - am Puls</h2>
  <div class="copy">
    <p>In dieser Rubrik wollen wir Sie nicht auf die Angebote unserer vier Pfarreien und des zukünftigen Pastoralraums, sondern auf den Inhalt unseres Glaubens aufmerksam machen.</p>
    <p>Dabei möchten wir Sie immer wieder überraschen: tiefsinnig oder humorvoll, mit einem Gedanken aus der reichen Tradition der Kirche oder einem zeitgenössischen Gedicht. Lassen Sie sich beschenken!</p>
    <p>Unter dieser Rubrik führen wir auch 'Grundgebete' der Kirche in deutscher und lateinischer Sprache sowie die 'basics' des katholischen Glaubens auf.</p>
  </div>
  <div class="picture" role="img" aria-label="Foto eines beleuchteten Altarraums in einer Basilika"></div>
</article>

<div class="news-badge" role="img" aria-label="Abzeichen"></div>

<section class="news row1">
  <div><strong>Hollbach</strong><em>Bruder Albin</em></div>
  <div><strong>Weltgebetstag</strong>Freitag, 7. März 2014, 19.00<br>katholische Kirchead</div>
  <div><strong>Rückblick Jubiläumsanlässe</strong>Neue Rubrik unter "Aktuelles"</div>
  <div><strong>Pfarrei Chronik</strong>Neue Rubrik unter "Aktuelles"</div>
</section>
<section class="news row2">
  <div><strong>Hollbach</strong><em>Bruder Albin</em></div>
  <div><strong>Weltgebetstag</strong>Freitag, 7. März 2014, 19.00<br>katholische Kirchead</div>
  <div><strong>Rückblick Jubiläumsanlässe</strong>Neue Rubrik unter "Aktuelles"</div>
  <div><strong>Pfarrei Chronik</strong>Neue Rubrik unter "Aktuelles"</div>
</section>

<footer class="bottom-bar">
  <svg width="14" height="22" viewBox="0 0 14 22"><path d="M3 9l4-5 4 5M3 15l4-5 4 5" stroke="#222" stroke-width="2" fill="none"/><path d="M7 15v6" stroke="#222" stroke-width="2"/></svg>
</footer>
</body>
</html>
```